Design a label for a dog shampoo names plovik, the sell point of this series of shampoo is “just like wash your dogs with milk, not harm for your hand ”, the style could be gentle or professional or even amazing.

Use only 2 colors in the design job, the color of our logo could be changed, it depends on your whole page. Please design in CDR or ai.

update:
Pls do more change with the fonts when you design the front page, including title and details. Try more styles of fonts. Addition, this design will be printed on the bottle, no a label stick on it.
Updates

Do not put a real dog or animal on the page, Pay more attention to the types of fonts

Reason: Expect for more design idea.

Target Market(s)

people 20-30 years old who have dogs and cats at home

Industry/Entity Type

It Professional

Requirements
Nice to have
• It would be nice if you add some detail words in the design of the right side.

```html
<!DOCTYPE html>
<html lang="en">
<head>
<meta charset="UTF-8">
<title>plovik — Super Conditioning Nutrient Shampoo</title>
<link rel="stylesheet" href="https://fonts.googleapis.com/css2?family=Jost:wght@400;500;700&display=swap">
<style>
  :root {
    --blue-deep: #4e8fc0;
    --blue-soft: #97c8e8;
    --paper: #ffffff;
  }
  html, body {
    margin: 0;
    padding: 0;
    width: 1200px;
    height: 2292px;
    overflow: hidden;
    background: var(--paper);
  }
  .label {
    position: relative;
    width: 1200px;
    height: 2292px;
    background: var(--paper);
    font-family: "Jost", "Futura", sans-serif;
  }
  .brand-name {
    position: absolute;
    margin: 0;
    color: var(--blue-soft);
    font-weight: 700;
    line-height: 1;
    letter-spacing: -8px;
  }
  .brand-name--top {
    left: 100px;
    top: 300px;
    width: 992px;
    font-size: 470px;
    text-align: center;
  }
  .brand-name--bottom {
    left: 587px;
    top: 820px;
    width: 521px;
    font-size: 430px;
    text-align: center;
  }
  .claims {
    position: absolute;
    right: 675px;
    top: 925px;
    margin: 0;
    color: var(--blue-deep);
    font-size: 51px;
    font-weight: 500;
    line-height: 83px;
    text-align: right;
  }
  .product-band {
    position: absolute;
    left: 108px;
    top: 1308px;
    width: 984px;
    height: 334px;
  }
  .product-band svg {
    position: absolute;
    inset: 0;
  }
  .product-title {
    position: absolute;
    inset: 0;
    margin: 0;
    display: flex;
    flex-direction: column;
    justify-content: center;
    align-items: center;
    color: var(--paper);
    font-size: 63px;
    font-weight: 400;
    letter-spacing: 9px;
    line-height: 104px;
  }
  .mascot-area {
    position: absolute;
    left: 408px;
    top: 1742px;
    width: 292px;
    height: 175px;
    border-radius: 88px;
    background: radial-gradient(circle at 60% 50%, var(--blue-deep) 0%, var(--blue-soft) 100%);
    opacity: 0.85;
  }
</style>
</head>
<body>
  <main class="label">
    <h1 class="brand-name brand-name--top">plov</h1>
    <p class="brand-name brand-name--bottom" aria-hidden="true">ik</p>

    <p class="claims">Moisture Rich<br>Smooth &amp; Silky<br>1000ml</p>

    <section class="product-band">
      <svg width="984" height="334" viewBox="0 0 984 334" aria-hidden="true">
        <path fill="var(--blue-deep)" d="M40 30
          C120 8 200 22 280 14 C360 6 440 26 520 14 C600 4 700 24 780 12
          C860 2 940 10 962 40 C984 80 960 120 976 170 C990 220 970 270 952 300
          C920 330 850 318 780 326 C700 334 620 318 540 326 C460 334 380 318 300 326
          C220 334 140 320 70 326 C20 326 8 290 18 250 C28 200 4 160 14 110
          C20 70 6 44 40 30 Z"/>
      </svg>
      <h2 class="product-title"><span>Super Conditioning</span><span>Nutrient Shampoo</span></h2>
    </section>

    <div class="mascot-area" role="img" aria-label="Small dog silhouette surrounded by bubbles"></div>
  </main>
</body>
</html>
```